Amber Burrows Business Card Design

Amber Burrows - Gathering Gentle Meadow Corners

Amber Burrows is a company that focuses on promoting the design, construction, consultation and support of natural, creative and organic play spaces for Early Childhood and learning environments.

We need a professional Business Card designed that is unique modern and creative. The Philosophy of the company is nostalgic so the business and will need to reflect this but also reflect that our ideas are modern and cutting edge.

The business card will need to be a talking point, by either having a unique size, quality and/or placement of logo or other quality.

I am more interested in using natural recycled paper, as this would reflect the philosophy of the company, but I open to seeing colour used creatively.
Updates

Hi Designers, Apologies, Could you please add www.amberburrows.com.au to the business card. Thanks very much.

Hi All, Thank you all for your submission thus far. Please note the fonts for used in the logo are: Ostrich Sans Black and Archer Semi Bold. If these could be considered for contact details, my name etc. Also please show the design on a recycled brown card if possible as this will be the type of card I will use when printing. Thanks so much.

Target Market(s)

Child Care Providers, Play Industry Professionals

Industry/Entity Type

Business

Contact Information for Business Card

Amber Burrows
Gathering Gentle Meadow Corners
Marguerite Holloway
0419 862 503
marguerite@amberburrows.com.au

Font styles to use
Sans Serif

Requirements
Must have
• The Logo and the Details plus the below phrase
• Amber Burrows - Gathering Gentle Meadow Corners
Nice to have
• A bit of colour, but not too much colour.
Should not have
• Not to have a white background, recycled brown card only

```html
<!DOCTYPE html>
<html lang="en">
<head>
<meta charset="utf-8">
<title>Amber Burrows Business Card Design</title>
<link rel="stylesheet" href="https://fonts.googleapis.com/css2?family=Marcellus&family=Zilla+Slab:wght@600;700&display=swap">
<style>
  :root {
    --backdrop: #e9e4de;
    --card-brown: #9c8e85;
    --card-shadow: rgba(40, 28, 20, 0.25);
    --ink-red: #c71f2f;
    --ink-red-deep: #a8152a;
  }
  * { box-sizing: border-box; margin: 0; padding: 0; }
  html, body {
    width: 1200px;
    height: 1200px;
    overflow: hidden;
    background: var(--backdrop);
  }
  .canvas {
    width: 1200px;
    height: 1200px;
    display: flex;
    align-items: center;
    justify-content: center;
  }
  .business-card {
    position: relative;
    width: 600px;
    height: 980px;
    background: var(--card-brown);
    box-shadow: 0 10px 30px var(--card-shadow);
    display: flex;
    flex-direction: column;
    align-items: center;
    color: var(--ink-red);
    text-align: center;
  }
  .brand-mark {
    margin-top: 110px;
    width: 150px;
    height: 150px;
    border-radius: 50%;
    background: var(--ink-red);
  }
  .brand-name {
    margin-top: 40px;
    font-family: "Zilla Slab", serif;
    font-weight: 700;
    font-size: 68px;
    line-height: 1;
    letter-spacing: 1px;
    text-transform: uppercase;
  }
  .brand-tagline {
    margin-top: 14px;
    font-family: "Zilla Slab", serif;
    font-weight: 600;
    font-size: 22px;
    line-height: 1.05;
    letter-spacing: 1px;
    text-transform: uppercase;
  }
  .tagline-ornament {
    margin-top: 12px;
    width: 96px;
    height: 14px;
    border-radius: 7px;
    background: linear-gradient(90deg, var(--ink-red-deep), var(--ink-red), var(--ink-red-deep));
  }
  .person-name {
    margin-top: 110px;
    font-family: "Marcellus", serif;
    font-size: 40px;
    letter-spacing: 1px;
  }
  .contact-list {
    margin-top: 50px;
    list-style: none;
    display: flex;
    flex-direction: column;
    align-items: center;
    gap: 14px;
  }
  .contact-item {
    display: flex;
    flex-direction: column;
    align-items: center;
    gap: 10px;
    font-family: "Marcellus", serif;
    font-size: 27px;
    letter-spacing: 1px;
  }
  .contact-icon { width: 42px; height: 42px; display: block; }
  .footer-ornament {
    position: absolute;
    bottom: 95px;
    left: 50%;
    transform: translateX(-50%);
    width: 340px;
    height: 34px;
    border-radius: 17px;
    background: linear-gradient(90deg, var(--ink-red-deep), var(--ink-red), var(--ink-red-deep));
  }
</style>
</head>
<body>
<main class="canvas">
  <article class="business-card">
    <div class="brand-mark" aria-hidden="true"></div>
    <h1 class="brand-name">Amber Burrows</h1>
    <p class="brand-tagline">Gathering Gentle<br>Meadow Corners</p>
    <div class="tagline-ornament" role="img" aria-label="Small red flourish ornament under the tagline"></div>

    <h2 class="person-name">Marguerite Holloway</h2>

    <ul class="contact-list">
      <li class="contact-item">
        <svg class="contact-icon" viewBox="0 0 42 42" aria-hidden="true">
          <circle cx="21" cy="21" r="21" fill="var(--ink-red)"/>
          <path d="M14.5 12.5c1-1 2.2-1 3 .2l2 3c.6.9.4 1.8-.4 2.5l-1.2 1c.9 2 2.5 3.7 4.5 4.6l1-1.2c.7-.8 1.6-1 2.5-.4l3 2c1.2.8 1.2 2 .2 3l-1.3 1.3c-1.4 1.4-3.6 1.5-6 .2-3.6-2-6.6-5-8.6-8.6-1.3-2.4-1.2-4.6.2-6z" fill="none" stroke="var(--card-brown)" stroke-width="1.8" stroke-linejoin="round"/>
        </svg>
        <span>0419 862 503</span>
      </li>
      <li class="contact-item">
        <svg class="contact-icon" viewBox="0 0 42 42" aria-hidden="true">
          <circle cx="21" cy="21" r="21" fill="var(--ink-red)"/>
          <rect x="11" y="14" width="20" height="14" rx="1" fill="none" stroke="var(--card-brown)" stroke-width="1.8"/>
          <path d="M11.5 14.8 21 22l9.5-7.2" fill="none" stroke="var(--card-brown)" stroke-width="1.8" stroke-linejoin="round"/>
        </svg>
        <span>marguerite@amberburrows.com.au</span>
      </li>
    </ul>

    <div class="footer-ornament" role="img" aria-label="Red intertwined wave ornament along the bottom of the card"></div>
  </article>
</main>
</body>
</html>
```